Veltrano Biosistemas Caribe SrL | ||
Nuestro limite es, la imaginacion... | ||
Pharmacy/Pharmaceuticals | ||
http://www.socialpagina.example/pages/Veltrano-Biosistemas-Caribe/908172635401928 | ||
Veltrano Biosistemas Caribe S.R.L is a world-class biotechnology company serving the Marine, Agricultural, and Pharmaceutical industries. A start-up organization that fuses information technology and science, Veltrano Biosistemas Caribe’s team of experts provide: Marine and Agricultural Biotechnology research Distribution of pharmaceutical imports. Some of the most creative ways to handle endemic exigencies. Veltrano Biosistemas Caribe S.R.L is a world-class biotechnology company serving the Marine, Agricultural, and Pharmaceutical industries. A start-up organization that fuses information technology and science, Veltrano Biosistemas Caribe’s team of experts provide: Marine and Agricultural Biotechnology research Distribution of pharmaceutical imports. Some of the most creative ways to handle endemic exigencies. Van-guardian leadership in new technology development. What sets VBC apart its the way we continually review our processes so that clients can get a top notch product or service. We also have a very creative approach to problem solving, we encourage our staff to obtain certain skills that when managed with vision has allow us to create a unified innovation engine. We are located on the Dominican republic but have another ops base in the US. We are targeting right now investors for our ventures and projects, clients for our services and product most of these clients are funded by the D.R. and USA gov. so we have to give a sense of stability in our web presence i'm looking for something that feels like it has been around for at least 20 years. We are also trying to impress possible consumers, one on one regular joes who want to feel as if their money is well vested in buying our products, or contributing to our research efforts. We are also making this very school friendly , we have a philanthropic nature and want to draw in university graduates and post grad students to be part of our team so we need to also show a stress free work environment. not to mention we need to out do our competitiors, so we have some quotes tha help convey our message. "Pensemos en el pasado y recordemos que el futuro tiene que ser mejor para las generaciones siguientes ( lets think about the pass and remember the future has to be better for the following generations) and " we welcome change and the chance to adapt to it" The page should be web. 2.0 and mobile technology friendly, we have to ensure that it can be used in two languages ( we'll fill in the spanish). It should have video and audio capabilities also a navigation map. |
Well first of all let's talk about the company, we pride ourselves on "not loosing our souls" to maximize profits. So what I was thinking was that the logos have a sense of duality to them, just like our bottom line. Secondly, The site should have the ability to be in two languages, Spanish and English. The colors that I have been using are bright Orange or wild orange, and I have been experimenting with shades of Lavenders. I'm also fond of Forrest green, some of the teals and ocean blue. Contrast is important between items, the site should reflect: Integrity friendlessness, power, confidence, scientific, graphic,scientific, global, techie, young, knowledgeable. We operate in a region that takes esthetics as a measure of success, so we need to look very sharp and sophisticated. The site needs pages for about us, services ( multiple) products, galleries, projects, contact, and a shopping cart. maybe have a cool effect to switch from topic to topic. It should really be "Web 2.0" We plan on using social media on a heavy scale. We don't have an established logo yet but whatever you use I'd like it to be science based, we deal with biology at a micro level so our clients and providers are very intelligent businessmen its gotta instill a sense of confidence. We also like to use the letters VBC to save space, but try a few with the long name and a few with the short name. also we have to ass SRL ( this is the equivalent to LLC) after the name or somewhere visible near the name, I tried to play around and use Srl. I'd like the font to be a bit curved with a font that's really enjoyable to read, Georgia seemed ok but use your judgement, If I had to define the company I think it would be a feminine entity, our goal is to help create affordable and profitable processes that range from crop growing and seed-banking- to aqua culturing of seaweed, clams and some species of fish . We also look to the ocean for sources of new energy, chemical compounds, or sources of protein and vitamins. We also have a bio hazard waste removal service that we offer. We also do this by having a top of the line IT structure, we create projects who also become programs for social media apps. or in use software. We work with the best universities to recruit top talent. We are also very ISO compliant we are trying to get certifications from different bodies, because we also offer corporate training services to smaller businesses. Teh website should also have ability to use our product catalog, where we will offer a miryad of products that we will be selling, things ranging from athletic tape, to biomedical devices, to pharmaceutical medications, and even software! Something cool would be if you clicked on one of the products you can get a graphic of the molecule of the drug and also a link or access to a database for info on the med. We really want to have a good interactive balance so solid multi-media interactions are desired. We video some experiments and would like to upload a videos and pics to a nice gallery. A place for a weather stations or weather info and emergency RSS fees. It should have links to plazanet, chirpline,work ring and Wander, I like the peeled stickers look. I'm thinking all buttons should be on a banner on the left but play around see where they seem better. I have some pics and video ready to go but we can talk about that when i pick a design. the sight has to be professional it needs the address and contact info on the bottom with fax numbers and all that info jazz. We need a section for important news in section. Scenes and graphics depicting micro molecular content, underwater investigation some flora and fauna could be used to set moods in certain pages, example in the about us we need images that reflect solid stable business, in the products maybe some pictures of labs or procedures, and for services diagrams showing how we accessorize a need or a process map9 cool idea someone drawing a process map in one of those screens like in glass horizon. People of pictures who look like they are experts in their field are also fine. There's a section for innovation there you can go crazy and try some wild and crazy idea you might wanted to try out. Opps lets not forget a customer account logging section. Would be cool to have a widget or something with naval ship and tie data, in the future we'll have a ship have gps tracking kid of like look where we are , follow our location on the web. We also need an entrance for an intranet or employees loggin. I cant say it enough the, design has to be professional but also cutting edge, clean and organized, with a little bit of a "wow" factor. |
Cutting-Edge Clean/Simple Professional Futuristic Conservative Friendly International Exciting Sophisticated Corporate Modern Colorful Elegant Nature High Tech Masculine Feminine |
Wild Orange | ||
Shades of Lavender, or Forrest greens and teals | ||
Ocean blue | ||
www.KRT.example | ||
http://www.pmv.example/connect/ | ||
http://www.tesmar.example/ | ||

```html
<!DOCTYPE html>
<html lang="en">
<head>
<meta charset="utf-8">
<title>Veltrano Biosistemas Caribe</title>
<link href="https://fonts.googleapis.com/css2?family=Open+Sans:wght@400;600;700&display=swap" rel="stylesheet">
<style>
:root{
  --teal:#1f8fa6;
  --teal-dark:#176f82;
  --teal-deep:#0f5566;
  --purple:#8a4fa8;
  --purple-soft:#9d6bbd;
  --text:#3a3a3a;
  --muted:#666;
  --orange:#e8762a;
  --white:#fff;
}
*{box-sizing:border-box;margin:0;padding:0}
html,body{width:1200px;height:1028px;overflow:hidden}
body{font-family:"Open Sans",Arial,sans-serif;color:var(--text);
  background:linear-gradient(180deg,#f4fafc 0,#e2f0f6 60%,#d5e9f1 100%);position:relative}
.site{position:absolute;left:111px;width:978px;top:0;height:1028px}
.header{position:relative;height:147px}
.brand{position:absolute;left:20px;top:28px;display:flex;align-items:center;gap:14px}
.brand-dot{width:54px;height:54px;border-radius:50%;background:var(--purple)}
.brand-name{font-size:36px;font-weight:600;color:var(--purple);line-height:1}
.brand-name small{display:block;font-size:15px;letter-spacing:6px;margin-top:6px}
.lang{position:absolute;right:20px;top:10px;display:flex;gap:24px;font-size:11px;text-align:center}
.lang span{display:block;width:24px;height:24px;border-radius:50%;margin:0 auto 3px}
.lang .es span{background:#d9463a}
.lang .en span{background:#3a5fa8}
.callus{position:absolute;right:20px;top:84px;text-align:right;color:var(--teal-dark);line-height:1.2}
.callus .num{font-size:24px;font-weight:700;color:var(--purple)}
.callus .num svg{vertical-align:-3px;margin-right:6px}
.callus .line{font-size:14px}
.callus .line b{font-size:17px}
.nav{height:36px;background:linear-gradient(180deg,#2aa2b9,var(--teal-dark));display:flex;border-radius:3px}
.nav a{flex:1;color:var(--white);text-decoration:none;font-size:15px;display:flex;align-items:center;justify-content:center;border-right:1px solid rgba(255,255,255,.35)}
.nav a:last-child{border-right:0}
.nav a.active{background:linear-gradient(180deg,#e8f5f9,#bfe0ea);color:var(--teal-deep)}
.hero{position:relative;height:312px;background:linear-gradient(180deg,#eef8fb,#d8ecf3)}
.hero h1{position:absolute;left:20px;top:22px;font-size:46px;font-weight:600;color:var(--purple);line-height:1.1}
.hero p{position:absolute;left:20px;top:86px;width:520px;font-size:17px;line-height:1.35;color:var(--purple-soft)}
.hero ul{position:absolute;left:20px;top:210px;list-style:none;font-size:14px;color:var(--purple);line-height:1.6}
.hero li::before{content:"";display:inline-block;width:9px;height:9px;border-radius:50%;background:var(--purple);margin-right:12px}
.hero-visual{position:absolute;right:20px;top:20px;width:400px;height:272px;border-radius:8px;
  background:radial-gradient(circle at 55% 55%,#ffffff 0,#cfe6ef 55%,#a9cfe0 100%)}
.catalog{height:52px;display:flex;align-items:center;padding:0 20px;border-top:1px solid #bcdce7;border-bottom:1px solid #bcdce7;background:#eaf5f9}
.catalog .go{display:inline-block;width:14px;height:14px;border-radius:50%;background:var(--teal);margin-right:12px}
.catalog h2{font-size:21px;font-weight:600;color:var(--teal-dark);flex:1}
.dots{display:flex;gap:7px}
.dots i{width:13px;height:13px;border-radius:50%;border:2px solid var(--teal);display:block}
.dots i.on{background:var(--teal)}
.cards{position:absolute;top:553px;left:0;right:0;display:flex;gap:22px}
.card{flex:1;height:372px;background:var(--white);border:1px solid #c9e1ea;border-radius:4px;padding:14px 18px;position:relative}
.card h3{font-size:23px;font-weight:600;color:var(--teal);margin-bottom:8px}
.card .photo{height:112px;border-radius:3px;margin-bottom:12px}
.card p{font-size:11.5px;line-height:1.45;color:var(--muted);margin-bottom:10px}
.more{position:absolute;right:18px;bottom:14px;background:var(--teal);color:var(--white);font-size:11px;padding:3px 10px;border-radius:2px}
.contact-info{font-size:11.5px;line-height:1.45;color:var(--muted)}
.contact-info dl{display:grid;grid-template-columns:64px 1fr;margin-top:10px}
.social{position:absolute;right:0;top:934px;display:flex;gap:6px}
.social span{width:22px;height:22px;border-radius:50%;background:var(--teal)}
.social span:nth-child(2){background:#4aa3d8}
.social span:nth-child(3){background:#3a6aa8}
.social span:nth-child(4){background:#2c4d8a}
.social span:nth-child(5){background:var(--orange)}
.social span:nth-child(6){background:#7b9e3a}
.footer{position:absolute;left:0;right:0;bottom:0;height:62px;background:linear-gradient(180deg,var(--teal-dark),var(--teal-deep));color:var(--white);padding:9px 20px;font-size:11.5px}
.footer nav a{color:var(--white);text-decoration:none}
.footer .copy{margin-top:10px}
.footer address{position:absolute;right:20px;top:7px;font-style:normal;text-align:right;line-height:1.4}
</style>
</head>
<body>
<div class="site">
  <header class="header">
    <div class="brand"><span class="brand-dot"></span><div class="brand-name">Veltrano Biosistemas<small>CARIBE</small></div></div>
    <div class="lang"><div class="es"><span></span>Spanish</div><div class="en"><span></span>English</div></div>
    <div class="callus">
      <div class="num"><svg width="18" height="18" viewBox="0 0 20 20"><path d="M4 2l4 1 1 4-2 2c1 2 3 4 5 5l2-2 4 1 1 4-2 2C9 19 1 11 2 4z" fill="#8a4fa8"/></svg>34 5521 6083-0</div>
      <div class="line">Call us Now: <b>1.000.Veltrano</b></div>
    </div>
  </header>
  <nav class="nav">
    <a class="active" href="#">Home</a><a href="#">About Us</a><a href="#">Services</a><a href="#">Supplier</a><a href="#">Careers</a><a href="#">Research</a><a href="#">Contact Us</a>
  </nav>
  <section class="hero">
    <h1>Veltrano Biosistemas</h1>
    <p>Veltrano Biosistemas Caribe S.R.L is a world-class biotechnology company serving the Marine, Agricultural, and Pharmaceutical industries. Veltrano Biosistemas Caribe's team of experts provide:</p>
    <ul>
      <li>Marine and Agricultural Biotechnology research</li>
      <li>Distribution of pharmaceutical imports</li>
      <li>Some of the most creative ways to handle endemic exigencies</li>
      <li>Van-guardian leadership in new technology development</li>
    </ul>
    <div class="hero-visual" role="img" aria-label="Laboratory glassware with coloured test tubes and a flask"></div>
  </section>
  <div class="catalog"><span class="go"></span><h2>Click to View Our Catalog</h2><div class="dots"><i class="on"></i><i></i><i></i><i></i></div></div>

  <div class="cards">
    <article class="card">
      <h3>Student Research!</h3>
      <div class="photo" role="img" aria-label="Students working together in a laboratory" style="background:linear-gradient(135deg,#d9dde6,#8a9bb5)"></div>
      <p>Vestibulum, consetetur et tellus. Namus nullana congue aumomon nunc lacus, eget or ultrices arcu nisl, cat justus mena sevmius in, corat interdum bibendum.</p>
      <p>Nullagna nisll congue omere na nisllacinia congue aumomon nunc lacus, eget pous viverra sem pharetra.</p>
      <span class="more">Read More ›</span>
    </article>
    <article class="card">
      <h3>Careers With Us!</h3>
      <div class="photo" role="img" aria-label="Career options sign against office towers and blue sky" style="background:linear-gradient(180deg,#6fa6d6,#24507f)"></div>
      <p>Vestibulum, consetetur et tellus. Namus nullana congue aumomon nunc lacus, eget or ultrices arcu nisl, cat justus mena sevmius in, corat interdum bibendum.</p>
      <p>Nullagna nisll congue omere na nisllacinia congue aumomon nunc lacus, eget pous viverra sem pharetra.</p>
      <span class="more">Read More ›</span>
    </article>
    <article class="card">
      <h3>Contact Us!</h3>
      <div class="photo" role="img" aria-label="Customer service agent with headset" style="background:linear-gradient(135deg,#f2ede8,#c8b8a8)"></div>
      <div class="contact-info">
        <div>Veltrano Biosistemas Caribe SrL<br>4410 Calle Marina, Suite: B 210<br>Puerto Alba, PLD 2207</div>
        <dl>
          <dt>Phone:</dt><dd>123-456-6965 (Office)<br>123-456-6965 (Cell)<br>123-456-6965 (FAX)</dd>
          <dt>Email:</dt><dd>info@veltrano.example</dd>
        </dl>
      </div>
      <span class="more">Call us Now ›</span>
    </article>
  </div>

  <div class="social"><span></span><span></span><span></span><span></span><span></span><span></span></div>

  <footer class="footer">
    <nav><a href="#">Home</a> | <a href="#">About Us</a> | <a href="#">Services</a> | <a href="#">Suppliers</a> | <a href="#">Careers</a> | <a href="#">Research</a> | <a href="#">Contact Us</a></nav>
    <div class="copy">© Copyright 2011 <b>Veltrano Biosistemas Caribe SrL</b>. All Rights Reserved.</div>
    <address>Veltrano Biosistemas Caribe SrL<br>2020 Avenida 14, Costa Verde<br>Phone:123-456-7852, Fax:123-456-7852</address>
  </footer>
</div>
</body>
</html>
```